Business Card template designs

We need a lot of Business card designs.
Your designs will get exposure on our newly opened business-card printing website.
We are committed to quality of paper and packages we use, so they will come up very fancy.

Here is your advantage. We will put the profile of the graphic designer on our site so that you can showcase your designs to people around the world and in Japan.

A profile is not mandatory, although we encourage graphic designers to have a profile to get continuous work in the future.
We are looking forward to having many good designs.

The right of the use of design will be owned by us.
The design may be used to the products other than
business cards.

Target Market(s)

designer,photographer,creator,artist

Industry/Entity Type

Printing

Contact Information for Business Card

The back design is important.
Please check the reference file.

Requirements
Must have
• Please include the following, required information on your business card designs.
• Name: Haruka Tanabe
• Title: Designer
• Web: https://www.korimo.co.jp/kr/
• Address: 4-17 Kitaharazono-Cho Nerima-ku, Tokyo
• Email: info@kkorimo.com
• Phone: 03 6184 3970
• Mobile: 070 4213 6087
• * For Japanese sites, we will convert the text portion to Japanese characters.
• * In case of 28mmx70mm only include Name,Enail,Phone and SNS account(https://www.facebook.com/kkorimo.com)
• 1. colorful
• 2. simple
• 3. natural
• 4. modern
• 5. cool
• 6. sporty
• Please make variations of the same image with 3-6
• different colors / patterns for one design so that
• customers can compare and choose.
• If you want to use a same picture, please make make
• copies and paste on each different types of design.
Nice to have
• You may also use, the following non-required information.
• Company Name: Korimo, Inc.
• Fax: 03-6471-2093
• Open space for company logo

```html
<!DOCTYPE html>
<html lang="en">
<head>
<meta charset="utf-8">
<title>Korimo business card</title>
<link rel="stylesheet" href="https://fonts.googleapis.com/css2?family=Arimo:wght@400;600&family=Oswald:wght@500&display=swap">
<style>
  :root {
    --bg: #2b2b2b;
    --orange: #f39322;
    --navy: #233a8c;
    --white: #ffffff;
    --grey: #5a5a5a;
    --body-font: "Arimo", Arial, sans-serif;
    --name-font: "Oswald", "Arial Narrow", sans-serif;
  }
  * { margin: 0; padding: 0; box-sizing: border-box; }
  html, body { width: 1200px; height: 900px; overflow: hidden; }
  body { background: var(--bg); font-family: var(--body-font); position: relative; }

  .card {
    position: absolute;
    width: 520px;
    height: 300px;
    box-shadow: 0 14px 30px rgba(0,0,0,.45);
  }

  /* Front */
  .card-front { left: 130px; top: 100px; background: var(--orange); }
  .brand {
    position: absolute;
    left: 150px; top: 112px;
    display: flex; align-items: center; gap: 12px;
  }
  .brand-name {
    font-family: var(--body-font);
    font-weight: 600;
    font-size: 56px;
    color: var(--navy);
    letter-spacing: 1px;
  }
  .brand-fax {
    position: absolute;
    left: 336px; top: 176px;
    display: flex; align-items: center; gap: 5px;
    color: var(--white);
    font-weight: 600;
    font-size: 12px;
  }
  .brand-fax svg { width: 11px; height: 11px; fill: var(--white); }

  /* Back */
  .card-back { left: 550px; top: 500px; background: var(--white); }
  .name-rule {
    position: absolute;
    left: 196px; right: 0; top: 118px;
    height: 4px;
    background: var(--navy);
  }
  .person { position: absolute; left: 36px; top: 100px; }
  .person-name {
    font-family: var(--name-font);
    font-weight: 500;
    font-size: 24px;
    line-height: 1;
    color: var(--orange);
    text-transform: uppercase;
  }
  .person-title { font-size: 13px; color: var(--grey); margin-top: 3px; }

  .contact-list {
    position: absolute; left: 36px; top: 158px;
    list-style: none;
  }
  .contact-list li {
    display: flex; align-items: center; gap: 10px;
    height: 20px;
    font-size: 14px;
    color: var(--navy);
  }
  .contact-list svg { width: 11px; height: 11px; fill: none; stroke: var(--orange); stroke-width: 2; }
  .address {
    position: absolute; left: 57px; top: 250px;
    font-size: 14px; line-height: 18px;
    color: var(--navy);
  }
</style>
</head>
<body>

<section class="card card-front" aria-label="Card front">
  <div class="brand"><span class="brand-name">Korimo</span></div>
  <div class="brand-fax">
    <svg viewBox="0 0 12 12" aria-hidden="true"><rect x="1" y="4" width="10" height="6" rx="1"/><rect x="3" y="1" width="6" height="3"/></svg>
    <span>03-6471-2093</span>
  </div>
</section>

<section class="card card-back" aria-label="Card back">
  <div class="name-rule"></div>
  <div class="person">
    <div class="person-name">Haruka Tanabe</div>
    <div class="person-title">Designer</div>
  </div>
  <ul class="contact-list">
    <li>
      <svg viewBox="0 0 12 12" aria-hidden="true"><path d="M2 1.5 L4 1.5 L5 4 L3.8 5 Q5 7.5 7 8.2 L8 7 L10.5 8 L10.5 10 Q5 11 1.5 3 Z"/></svg>
      <span>03 6184 3970</span>
    </li>
    <li>
      <svg viewBox="0 0 12 12" aria-hidden="true"><rect x="3" y="1" width="6" height="10" rx="1"/></svg>
      <span>070 4213 6087</span>
    </li>
    <li>
      <svg viewBox="0 0 12 12" aria-hidden="true"><rect x="1" y="2.5" width="10" height="7"/><path d="M1 2.5 L6 6.5 L11 2.5"/></svg>
      <span>info@kkorimo.com</span>
    </li>
    <li>
      <svg viewBox="0 0 12 12" aria-hidden="true"><circle cx="6" cy="6" r="5"/><path d="M1 6 H11 M6 1 Q3 6 6 11 Q9 6 6 1"/></svg>
      <span>www.korimo.co.jp/kr/</span>
    </li>
  </ul>
  <p class="address">4-17 Kitaharazono-Cho<br>Nerima-ku, Tokyo</p>
</section>

</body>
</html>
```